New Zealand Marlborough Sauvignon Blanc wine packaging design

We need packaging design for our new wine brand, Dunmore Hale. The wine is a New Zealand Marlborough Sauvignon Blanc. We would like the packaging will portray elegance and style with an understated label. We are looking for a label that portrays the elegance of the French Riviera. The label should be round or pill shaped.
Updates

Industry/Entity Type

Wine

Font styles to use
Serif
Sans Serif

Requirements
Must have
• The words in order of importance: Dunmore Hale, Sauvignon Blanc, Marlborough, New Zealand. It should be fit to the bottle posted in the links
Nice to have
• a pill shape or circular shape
Should not have
• Illustrations of wine bottles, wine glasses, or grapes

```html
<!DOCTYPE html>
<html lang="en">
<head>
<meta charset="utf-8">
<title>Dunmore Hale Sauvignon Blanc Label</title>
<link rel="stylesheet" href="https://fonts.googleapis.com/css2?family=Cinzel:wght@400;500&family=Montserrat:wght@500;600;700&display=swap">
<style>
  :root {
    --page-bg: #d2d2d2;
    --label-paper: #f7f7f7;
    --frame-line: #5e5e5e;
    --band-grey: #b3b3b3;
    --band-text: #ffffff;
    --rose: #a2525c;
    --ink: #2e2e2e;
    --sketch-grey: #c9c9c9;
  }
  * { margin: 0; padding: 0; box-sizing: border-box; }
  html, body {
    width: 1200px; height: 1200px; overflow: hidden;
    background: var(--page-bg);
  }
  .label {
    position: absolute; left: 362px; top: 75px;
    width: 476px; height: 1050px;
  }
  .label-shape { position: absolute; inset: 0; }
  .label-text {
    position: absolute; left: 0; width: 100%;
    text-align: center;
  }
  .brand {
    font-family: "Cinzel", serif;
    font-weight: 400;
    color: var(--rose);
    font-size: 60px;
    line-height: 68px;
    letter-spacing: 1px;
    top: 160px;
  }
  .varietal {
    font-family: "Montserrat", sans-serif;
    font-weight: 600;
    color: var(--band-text);
    font-size: 27px;
    line-height: 52px;
    top: 379px;
  }
  .region {
    font-family: "Montserrat", sans-serif;
    font-weight: 700;
    color: var(--rose);
    font-size: 27px;
    letter-spacing: 0.5px;
    top: 492px;
  }
  .country {
    font-family: "Cinzel", serif;
    font-weight: 500;
    color: var(--ink);
    font-size: 28px;
    letter-spacing: 1px;
    top: 560px;
  }
  .volume {
    font-family: "Montserrat", sans-serif;
    font-weight: 500;
    color: var(--ink);
    font-size: 20px;
    text-align: right;
    left: auto; right: 44px; width: auto;
    top: 992px;
  }
</style>
</head>
<body>
  <div class="label">
    <svg class="label-shape" width="476" height="1050" viewBox="0 0 476 1050">
      <defs>
        <linearGradient id="harbour-tone" x1="0" y1="0" x2="1" y2="0.3">
          <stop offset="0" stop-color="#c4c4c4"/>
          <stop offset="0.6" stop-color="#e2e2e2"/>
          <stop offset="1" stop-color="#f7f7f7" stop-opacity="0"/>
        </linearGradient>
      </defs>
      <path d="M0,1050 V238 A238,238 0 0 1 476,238 V1050 Z" fill="var(--label-paper)"/>
      <path d="M14,1036 V238 A224,224 0 0 1 462,238 V1036 Z" fill="none" stroke="var(--frame-line)" stroke-width="2"/>
      <rect class="ornament-top" x="148" y="124" width="180" height="8" fill="var(--rose)" opacity="0.35" role="img" aria-label="Scroll flourish ornament"/>
      <rect class="ornament-bottom" x="148" y="312" width="180" height="8" fill="var(--rose)" opacity="0.35" role="img" aria-label="Scroll flourish ornament"/>
      <rect class="varietal-band" x="14" y="379" width="448" height="52" fill="var(--band-grey)"/>
      <line x1="14" y1="376" x2="462" y2="376" stroke="var(--frame-line)" stroke-width="2"/>
      <line x1="14" y1="434" x2="462" y2="434" stroke="var(--frame-line)" stroke-width="2"/>
      <rect class="harbour-sketch" x="16" y="605" width="420" height="380" fill="url(#harbour-tone)" role="img" aria-label="Line sketch of a Riviera harbour town with hills and moored boats"/>
    </svg>
    <div class="label-text brand">DUNMORE<br>HALE</div>
    <div class="label-text varietal">SAUVIGNON BLANC</div>
    <div class="label-text region">MARLBOROUGH</div>
    <div class="label-text country">NEW ZEALAND</div>
    <div class="label-text volume">750 ML</div>
  </div>
</body>
</html>
```